Copper Ridge Business Cards For New Startup

I am looking for you to design some business cards for a new startup https://copperridgehub.example. I have supplied logo, brand guidelines and our signatures as a guide.

We need this to reflect the brand guidelines and the website for brand consistency,

What is Copper Ridge?

Mallorca's Business Growth Community
Join your new business community full of passionate entrepreneurs who
love to solve problems and help each other grow together!

Any questions you can ask.

Target Market(s)

Business to Business

Contact Information for Business Card

These are attached (signatures) to the job

Font styles to use
Other font styles liked:
• Open Sans

Requirements
Must have
• Match design guidelines
Nice to have
• Photos of our faces so people remember us

```html
<!DOCTYPE html>
<html lang="en">
<head>
<meta charset="utf-8">
<title>Copper Ridge Business Cards</title>
<link href="https://fonts.googleapis.com/css2?family=Open+Sans:wght@400;600;700&display=swap" rel="stylesheet">
<style>
  :root {
    --brand-green: #686b2e;
    --brand-green-dark: #5c6028;
    --brand-text: #5e6328;
    --ink: #1e1e1e;
    --paper: #ffffff;
    --paper-shade: #ececec;
    --canvas: #ffffff;
  }
  * { box-sizing: border-box; margin: 0; padding: 0; }
  html, body { width: 1200px; height: 805px; overflow: hidden; background: var(--canvas); }
  body { position: relative; font-family: "Open Sans", Arial, sans-serif; }

  .card {
    position: absolute; width: 445px; height: 256px; border-radius: 14px; overflow: hidden;
    box-shadow: 0 1px 4px rgba(0,0,0,.28);
  }
  .card--front { background: linear-gradient(180deg, var(--paper-shade) 0%, var(--paper) 60%); }
  .card--back { background: linear-gradient(160deg, var(--brand-green-dark) 0%, var(--brand-green) 55%, #6b6f31 100%); }

  .back-ring { position: absolute; left: -45px; top: -70px; width: 270px; height: 270px; border-radius: 50%;
    border: 22px solid rgba(0,0,0,.045); box-shadow: inset 0 0 0 1px rgba(255,255,255,.03); }

  .front-band { position: absolute; left: 0; right: 0; top: 168px; bottom: 0; background: var(--brand-green); }

  .brand { position: absolute; display: flex; align-items: center; white-space: nowrap; }
  .brand__dot { border-radius: 50%; flex: none; }
  .brand--front { right: 27px; top: 24px; gap: 10px; }
  .brand--front .brand__dot { width: 36px; height: 36px; border: 1.6px solid var(--brand-text); }
  .brand--front .brand__name { color: var(--brand-text); font-size: 19px; font-weight: 600; letter-spacing: .1px; }
  .brand--back { left: 93px; top: 100px; gap: 18px; }
  .brand--back .brand__dot { width: 56px; height: 56px; border: 1.8px solid #fff; }
  .brand--back .brand__name { color: #fff; font-size: 27px; font-weight: 600; letter-spacing: .2px; }

  .portrait { position: absolute; left: 37px; top: 83px; width: 104px; height: 119px;
    clip-path: polygon(50% 0, 100% 25%, 100% 75%, 50% 100%, 0 75%, 0 25%); background: #fff;
    filter: drop-shadow(0 1px 2px rgba(0,0,0,.25)); }
  .portrait__fill { position: absolute; inset: 3px;
    clip-path: polygon(50% 0, 100% 25%, 100% 75%, 50% 100%, 0 75%, 0 25%); }
  .portrait--one .portrait__fill {
    background: radial-gradient(ellipse 36% 30% at 50% 42%, #c79a82 0%, rgba(199,154,130,0) 100%),
                linear-gradient(180deg, #d9d8d4 0%, #c8c6c2 45%, #8a96a8 80%, #5f6f86 100%); }
  .portrait--two .portrait__fill {
    background: radial-gradient(ellipse 34% 32% at 50% 52%, #e2b39c 0%, rgba(226,179,156,0) 100%),
                linear-gradient(180deg, #d6bb86 0%, #e1c896 40%, #d4b08a 70%, #9b8f88 100%); }

  .identity { position: absolute; right: 27px; top: 126px; text-align: right; white-space: nowrap; }
  .identity__name { color: var(--ink); font-size: 16px; font-weight: 400; letter-spacing: .1px; line-height: 20px; }
  .identity__role { color: var(--brand-text); font-size: 10.5px; line-height: 14px; letter-spacing: -.1px; }

  .contacts { position: absolute; right: 26px; top: 178px; list-style: none; }
  .contacts li { display: flex; justify-content: flex-end; align-items: center; gap: 10px; height: 19px;
    color: #fff; font-size: 11px; white-space: nowrap; }
  .contacts svg { width: 13px; height: 11px; flex: none; }

  .social { position: absolute; left: 47px; top: 216px; display: flex; gap: 4px; }
  .social span { width: 14px; height: 14px; background: #f4f4ee; display: block; position: relative; }
  .social span::after { content: ""; position: absolute; inset: 4px; background: var(--brand-green); border-radius: 1px; }

  .pos-a { left: 124px; } .pos-b { left: 633px; }
  .row-1 { top: 99px; } .row-2 { top: 406px; }
</style>
</head>
<body>
<svg width="0" height="0" style="position:absolute">
  <defs>
    <symbol id="icon-phone" viewBox="0 0 13 11"><path d="M1 3.5C1 1.8 3.5 1 6.5 1S12 1.8 12 3.5V4.5H9.3V3.2H3.7V4.5H1Z" fill="#fff"/><path d="M3 5h7l2 5H1Z" fill="#fff"/></symbol>
    <symbol id="icon-mail" viewBox="0 0 13 11"><rect x="1" y="1.5" width="11" height="8" fill="#fff"/><path d="M1 1.5l5.5 4.5 5.5-4.5" fill="none" stroke="#686b2e" stroke-width="1"/></symbol>
    <symbol id="icon-globe" viewBox="0 0 13 11"><g fill="none" stroke="#fff" stroke-width=".9"><circle cx="6.5" cy="5.5" r="4.6"/><ellipse cx="6.5" cy="5.5" rx="2" ry="4.6"/><path d="M1.9 5.5h9.2M2.6 3h7.8M2.6 8h7.8"/></g></symbol>
  </defs>
</svg>

<article class="card card--front pos-a row-1">
  <div class="front-band"></div>
  <div class="brand brand--front"><span class="brand__dot"></span><span class="brand__name">COPPER RIDGE</span></div>
  <div class="portrait portrait--one"><div class="portrait__fill" role="img" aria-label="Portrait photo of Daniel Rowe"></div></div>
  <div class="identity">
    <p class="identity__name">DANIEL ROWE</p>
    <p class="identity__role">FOUNDER AND GROWTH HACKER&nbsp; I &nbsp;COPPER RIDGE</p>
  </div>
  <ul class="contacts">
    <li>+34 600 555 012 <svg><use href="#icon-phone"/></svg></li>
    <li>dr@copperridgehub.example <svg><use href="#icon-mail"/></svg></li>
    <li>copperridgehub.example <svg><use href="#icon-globe"/></svg></li>
  </ul>
  <div class="social" aria-label="Social profiles"><span></span><span></span><span></span><span></span><span></span></div>
</article>

<article class="card card--front pos-b row-1">
  <div class="front-band"></div>
  <div class="brand brand--front"><span class="brand__dot"></span><span class="brand__name">COPPER RIDGE</span></div>
  <div class="portrait portrait--two"><div class="portrait__fill" role="img" aria-label="Portrait photo of Helena Marsh"></div></div>
  <div class="identity">
    <p class="identity__name">HELENA MARSH</p>
    <p class="identity__role">RELATIONSHIP DIRECTOR&nbsp; I &nbsp;COPPER RIDGE</p>
  </div>
  <ul class="contacts">
    <li>+44 7700 900 123 <svg><use href="#icon-phone"/></svg></li>
    <li>hm@copperridgehub.example <svg><use href="#icon-mail"/></svg></li>
    <li>copperridgehub.example <svg><use href="#icon-globe"/></svg></li>
  </ul>
  <div class="social" aria-label="Social profiles"><span></span><span></span><span></span><span></span><span></span></div>
</article>

<article class="card card--back pos-a row-2">
  <div class="back-ring"></div>
  <div class="brand brand--back"><span class="brand__dot"></span><span class="brand__name">COPPER RIDGE</span></div>
</article>

<article class="card card--back pos-b row-2">
  <div class="back-ring"></div>
  <div class="brand brand--back"><span class="brand__dot"></span><span class="brand__name">COPPER RIDGE</span></div>
</article>
</body>
</html>
```